"Bright Hollow Craft Dwellings" need a busines Card Design got Builder

We need a business card design for a company based in Milford, Michigancalled Bright Hollow Craft Dwellings - has been recognized as a premier custom home builder. Distinguished by outstanding craftmanship and timeless beauty. Our custom home can be found in the most prestigious communities in Michigan. The homes are built with ICF (insulated concrete homes) which is green, allergy free, fire free, mold free and quitter. Our slogan "building one dream at a Time" and also we are ICF distributor for the state of Michigan

Target Market(s)

Anyone who is making over $100,000 a year and who wants to have totally custom built home. Ages from 29 up to 60 years old

Industry/Entity Type

Concrete

Contact Information for Business Card

we want to use - green, black, gray or blue colors - we want to look different with our business cards, because we built homes only with ICF, green, healthier and highly energy efficient homes.

Requirements
Must have
• I have logo that I attached and we have been using the logo (the only green home)
Nice to have
• should look quality business card,

```html
<!DOCTYPE html>
<html lang="en">
<head>
<meta charset="utf-8">
<title>Bright Hollow Craft Dwellings — Business Card</title>
<link rel="stylesheet" href="https://fonts.googleapis.com/css2?family=Jost:wght@300;400&display=swap">
<style>
  :root {
    --backdrop: #4b4b4b;
    --brand-green: #8bc43f;
    --card-white: #ffffff;
    --text-gray: #5a5a5a;
    --rule-gray: #9aa38a;
    --logo-gray: #6d6d6d;
  }
  * { margin: 0; padding: 0; box-sizing: border-box; }
  html, body {
    width: 1200px; height: 1000px; overflow: hidden;
    background: var(--backdrop);
    font-family: "Jost", sans-serif;
  }
  .canvas { position: relative; width: 1200px; height: 1000px; }

  .card {
    position: absolute;
    border-radius: 14px;
    overflow: hidden;
    box-shadow: 0 6px 10px rgba(0,0,0,0.35);
  }
  .card-front {
    left: 185px; top: 158px; width: 559px; height: 344px;
    background: var(--brand-green);
  }
  .card-back {
    left: 464px; top: 529px; width: 560px; height: 346px;
    background: var(--card-white);
  }

  .brand-mark {
    position: absolute;
    display: flex; align-items: center; gap: 22px;
  }
  .brand-dot { border-radius: 50%; flex: none; }
  .brand-name {
    font-weight: 300;
    text-transform: uppercase;
    line-height: 0.95;
    letter-spacing: 0.02em;
  }
  .card-front .brand-mark { left: 88px; top: 118px; }
  .card-front .brand-dot { width: 100px; height: 100px; background: var(--card-white); }
  .card-front .brand-name { color: var(--card-white); font-size: 23px; }

  .card-back .brand-mark { left: 36px; top: 40px; }
  .card-back .brand-dot { width: 98px; height: 98px; background: var(--brand-green); }
  .card-back .brand-name { color: var(--logo-gray); font-size: 22px; }

  .holder {
    position: absolute; right: 41px; top: 160px; text-align: right;
  }
  .holder-name { color: var(--brand-green); font-size: 21px; font-weight: 400; }
  .holder-title { color: var(--text-gray); font-size: 12px; margin-top: 2px; }
  .holder-rule {
    position: absolute; left: 41px; top: 197px; width: 417px; height: 1px;
    background: var(--rule-gray);
  }

  .contact-list {
    position: absolute; left: 41px; top: 234px; list-style: none;
    color: var(--text-gray); font-size: 13px;
  }
  .contact-list li { display: flex; align-items: center; gap: 6px; height: 21px; }
  .contact-list svg { width: 14px; height: 14px; fill: var(--brand-green); }

  .address {
    position: absolute; left: 336px; top: 234px;
    color: var(--text-gray); font-size: 13px; font-style: normal; line-height: 21px;
  }
  .address .company { color: var(--brand-green); }

  .slogan-band {
    position: absolute; left: 0; bottom: 0; width: 100%; height: 27px;
    background: var(--brand-green);
    color: var(--card-white);
    font-size: 14px; letter-spacing: 0.72em;
    display: flex; align-items: center; justify-content: center;
    padding-left: 0.72em;
  }
</style>
</head>
<body>
<main class="canvas">
  <section class="card card-front">
    <div class="brand-mark">
      <span class="brand-dot"></span>
      <span class="brand-name">Bright Hollow<br>Craft Dwellings</span>
    </div>
  </section>

  <section class="card card-back">
    <div class="brand-mark">
      <span class="brand-dot"></span>
      <span class="brand-name">Bright Hollow<br>Craft Dwellings</span>
    </div>

    <div class="holder">
      <div class="holder-name">Marcus Elden</div>
      <div class="holder-title">President</div>
    </div>
    <div class="holder-rule"></div>

    <ul class="contact-list">
      <li>
        <svg viewBox="0 0 24 24"><path d="M6.6 10.8a15 15 0 0 0 6.6 6.6l2.2-2.2a1 1 0 0 1 1-.25 11.4 11.4 0 0 0 3.6.57 1 1 0 0 1 1 1V20a1 1 0 0 1-1 1A17 17 0 0 1 3 4a1 1 0 0 1 1-1h3.5a1 1 0 0 1 1 1c0 1.25.2 2.45.57 3.6a1 1 0 0 1-.25 1z"/></svg>
        248 555 0147
      </li>
      <li>
        <svg viewBox="0 0 24 24"><path d="M2 5h20v14H2z M3 6l9 7 9-7" fill="none" stroke="#8bc43f" stroke-width="0"/><path d="M2 5h20v2l-10 7L2 7z M2 9l10 7 10-7v10H2z"/></svg>
        info@brighthollow.com
      </li>
      <li>
        <svg viewBox="0 0 24 24"><path d="M12 2a10 10 0 1 0 0 20 10 10 0 0 0 0-20zm0 2c1 0 2.4 2 3 5H9c.6-3 2-5 3-5zM4.3 9h2.8a17 17 0 0 0 0 6H4.3a8 8 0 0 1 0-6zm4.7 0h6a15 15 0 0 1 0 6H9a15 15 0 0 1 0-6zm7.9 0h2.8a8 8 0 0 1 0 6h-2.8a17 17 0 0 0 0-6zM9 17h6c-.6 3-2 5-3 5s-2.4-2-3-5z"/></svg>
        www.brighthollowdwellings.com
      </li>
    </ul>

    <address class="address">
      <span class="company">Bright Hollow Craft Dwellings</span><br>
      P.O Box 418 Cedarline St.<br>
      Milford MI 48381
    </address>

    <div class="slogan-band">BUILDING ONE DREAM AT A TIME</div>
  </section>
</main>
</body>
</html>
```